Animal Horse & Bedding Company Needs a Website Coded & Designed

We need a website for a new animal bedding and feed company that is visually grabbing and vibrant. We would like to see a website that displays trust, quality and confidence. Needs to be responsive and mobile friendly for all browsers and coded for both Android & IOS. SEO is also important.

Joomla or Wordpress – must be both desktop and mobile friendly with fast page load speed. Need the ability to edit ourselves in Wordpress or Joomla.

Full details attached below with some layout and content ideas.

Coding

Coded - Design and coding required

Number of Pages Required

5+ page

Font styles to use
Sans Serif

Requirements
Must have
• Needs to be responsive and mobile friendly for all browsers and coded for both Android & IOS. SEO is also important.

Wordpress – must be both desktop and mobile friendly with fast page load speed. Need the ability to edit ourselves in Wordpress.

Logo Colours:
Dark Brown
CMYK: 50 / 70 / 80 / 70
Pantone: 4625C

Orange
CMYK: 0 / 50 / 100 / 0
Pantone: 144C
Nice to have
• Use picture of building attached and super impose logo on building.

```html
<!DOCTYPE html>
<html lang="en">
<head>
<meta charset="utf-8">
<title>About Us – Golden Bale Bedding &amp; Feed</title>
<link href="https://fonts.googleapis.com/css2?family=Montserrat:wght@300;400;500;600;700;800&display=swap" rel="stylesheet">
<style>
:root{
  --orange:#f7941d;
  --brown:#3b2314;
  --ink:#1a1a1a;
  --text:#555;
  --muted:#999;
  --light:#f5f5f5;
  --line:#d9d9d9;
  --white:#fff;
}
*{box-sizing:border-box;margin:0;padding:0}
html,body{width:1200px;height:3130px;overflow:hidden}
body{font-family:'Montserrat',sans-serif;color:var(--text);background:var(--white);position:relative}
.wrap{width:856px;margin:0 auto;position:relative}
.btn{display:inline-block;background:var(--orange);color:var(--white);font-weight:600;border-radius:3px;text-decoration:none}

/* header */
.site-header{height:62px}
.site-header .wrap{display:flex;align-items:center;height:62px;justify-content:space-between}
.brand{display:flex;align-items:center;gap:8px;font-weight:700;font-size:19px;color:var(--brown);letter-spacing:.5px}
.brand-dot{width:26px;height:26px;border-radius:50%;background:var(--orange)}
.nav{display:flex;align-items:center;gap:33px;font-size:13px;color:#333}
.nav a{color:inherit;text-decoration:none;position:relative}
.nav a.active{color:var(--orange)}
.nav a.active::after{content:"";position:absolute;left:50%;bottom:-8px;width:16px;height:2px;margin-left:-8px;background:var(--orange)}
.nav .btn{padding:7px 15px;font-size:13px;margin-left:-2px}

/* hero */
.hero{height:343px;background:linear-gradient(90deg,#4a3a22 0%,#8a6a38 35%,#b08a48 55%,#6e6a45 75%,#2a2418 100%);position:relative}
.hero-photo{position:absolute;inset:0}
.hero .wrap{padding-top:80px;color:var(--white)}
.hero h1{font-size:46px;font-weight:800;letter-spacing:-.5px;margin-bottom:22px}
.hero p{font-size:15px;line-height:16px;width:300px;margin-bottom:28px}
.hero .btn{padding:6px 15px;font-size:13px}

/* welcome */
.welcome{padding-top:100px;text-align:center}
.welcome .kicker{font-size:15px;color:#666;font-weight:400}
.welcome h2{font-size:24px;font-weight:700;color:var(--ink);letter-spacing:-.5px;margin:4px 0 20px}
.welcome p{font-size:10px;line-height:15px;font-weight:300;color:#666;width:690px;margin:0 auto 18px}
.pig-photo{height:369px;margin-top:22px;border-radius:4px;background:radial-gradient(ellipse at 50% 40%,#e4b9a2 0%,#c89a7c 35%,#a88660 65%,#7c6846 100%)}

/* story */
.story{background:var(--light);margin-top:97px;height:573px}
.story .wrap{display:flex;justify-content:space-between;padding-top:104px}
.story-text{width:425px;padding-top:24px}
.story-text p{font-size:10px;line-height:15px;font-weight:300;color:#666;margin-bottom:15px}
.story-text .btn{margin-top:24px;padding:6px 16px;font-size:11px}
.rabbit-photo{width:367px;height:366px;border-radius:4px;background:linear-gradient(180deg,#2f5a24 0%,#4f8a2c 45%,#9cc84a 80%,#b9d85a 100%)}

/* quote */
.quote{padding-top:97px}
.quote-card{border:1px solid var(--line);border-radius:8px;height:431px;padding:34px 37px 0}
.quote-card h2{text-align:center;font-size:24px;font-weight:700;color:var(--ink);letter-spacing:-.5px;margin-bottom:28px}
.field-row{display:flex;gap:16px;margin-bottom:12px}
.field{flex:1;height:38px;border:1px solid var(--line);border-radius:3px;font-size:9px;color:#aaa;padding:13px 16px}
.field.area{height:140px}
.quote-card .btn{display:block;width:197px;height:37px;line-height:37px;text-align:center;font-size:12px;margin:20px auto 0}

/* testimonial */
.testimonial{margin-top:97px;height:420px;background:radial-gradient(ellipse at 75% 35%,#5a4a30 0%,#3a3020 40%,#24200f 100%);color:var(--white);text-align:center;position:relative}
.testimonial .wrap{padding-top:100px}
.testimonial h2{font-size:24px;font-weight:700;letter-spacing:-.5px;margin-bottom:30px}
.testimonial h3{font-size:15px;font-weight:600}
.testimonial .role{font-size:10px;margin:3px 0 25px}
.testimonial .quote-text{font-size:10px;line-height:15px;width:490px;margin:0 auto}
.arrow{position:absolute;top:245px}
.arrow.prev{left:246px}.arrow.next{right:246px}
.dots{display:flex;justify-content:center;gap:6px;margin-top:32px}
.dots span{width:9px;height:9px;border-radius:50%;border:1px solid var(--white)}
.dots span.on{background:var(--white)}

/* footer */
.site-footer{background:var(--light);height:273px}
.site-footer .wrap{display:flex;padding-top:90px}
.foot-brand{width:262px}
.foot-brand .brand{font-size:16px}
.foot-brand p{font-size:9px;line-height:11px;color:#666;width:160px;margin-top:22px}
.foot-col h4{font-size:15px;font-weight:600;color:var(--ink);margin-bottom:18px}
.foot-col ul{list-style:none;font-size:9px;color:#777;line-height:21px}
.foot-menu{width:170px;padding-top:0}
.foot-contact{width:226px}
.foot-contact li{line-height:13px;margin-bottom:8px}
.socials{display:flex;gap:14px;margin-bottom:24px}
.socials span{width:8px;height:8px;border-radius:50%;background:#888}
.socials span.on{background:var(--orange)}
.subscribe-input{width:197px;height:28px;background:var(--white);font-size:8px;color:#aaa;display:flex;align-items:center;gap:8px;padding-left:10px;margin-bottom:3px}
.subscribe-btn{width:197px;height:28px;line-height:28px;text-align:center;font-size:9px;font-weight:500;background:var(--orange);color:var(--white);border-radius:2px}
.copyright{position:absolute;top:3083px;left:0;width:1200px;border-top:1px solid var(--line);text-align:center;font-size:9px;color:#555;padding-top:16px}
</style>
</head>
<body>

<header class="site-header">
  <div class="wrap">
    <div class="brand"><span class="brand-dot"></span>GOLDEN BALE</div>
    <nav class="nav">
      <a href="#">Home</a>
      <a href="#" class="active">About Us</a>
      <a href="#">Feed</a>
      <a href="#">Bedding</a>
      <a href="#">Contact</a>
      <a href="#" class="btn">Get a Quote</a>
    </nav>
  </div>
</header>

<section class="hero">
  <div class="hero-photo" role="img" aria-label="Sheep standing in a sunlit autumn meadow"></div>
  <div class="wrap">
    <h1>About Us</h1>
    <p>Golden Bale offers supply and delivery of fresh bedding as well as removal of waste bedding.</p>
    <a href="#" class="btn">Get a Quote</a>
  </div>
</section>

<section class="welcome">
  <div class="wrap">
    <div class="kicker">Welcome to</div>
    <h2>Golden Bale</h2>
    <p>Golden Bale is a locally owned company located in Millbrook, AB. We are dedicated in providing high quality products and services. Producing, buying and marketing hay and straw for x amount of years. Insert blub on ownership/history of key staff/owners.</p>
    <p>Golden Bale offers supply and delivery of fresh bedding as well as removal of waste bedding. Let us deliver you a container of fresh straw and haul your waste bedding away. A full service solution that is sustainable and responsible.</p>
    <p>Your animal deserves the very best in health and comfort to keep them healthy, strong and happy. Our products are designed for horses, livestock (goats, cattle and sheep), small caged animals (rabbits, guinea pigs and more).</p>
    <div class="pig-photo" role="img" aria-label="Young pigs on straw bedding"></div>
  </div>
</section>

<section class="story">
  <div class="wrap">
    <div class="story-text">
      <p>For many people, their animals, whether it be a horse, goat or other are more than just an animal, they are a part of your family, a way of life, and their comfort is important. Fine cut 100% chopped straw offers a softer bedding for your equine or other large and/or small animal.</p>
      <p>This straw bedding is light weight which allows for easier spreading, removing and hauling away. Straw also decomposes a lot faster than wood shavings and makes for great compost material.</p>
      <p>For many people, their animals, whether it be a horse, goat or other are more than just an animal, they are a part of your family, a way of life, and their comfort is important. Fine cut 100% chopped straw offers a softer bedding for your equine or other large and/or small animal.</p>
      <p>This straw bedding is light weight which allows for easier spreading, removing and hauling away. Straw also decomposes a lot faster than wood shavings and makes for great compost material.</p>
      <a href="#" class="btn">Get A Quote</a>
    </div>
    <div class="rabbit-photo" role="img" aria-label="Two rabbits sitting in green grass"></div>
  </div>
</section>

<section class="quote">
  <div class="wrap">
    <form class="quote-card">
      <h2>Request a Quote</h2>
      <div class="field-row"><div class="field">First Name*</div><div class="field">Last Name*</div></div>
      <div class="field-row"><div class="field">Email Address*</div><div class="field">Contact Number*</div></div>
      <div class="field-row"><div class="field area">Requirements*</div></div>
      <a href="#" class="btn">Send Message</a>
    </form>
  </div>
</section>

<section class="testimonial" role="img" aria-label="Dimmed photo of lambs in a field behind client testimonial">
  <svg class="arrow prev" width="8" height="14" viewBox="0 0 8 14"><path d="M7 1L1 7l6 6" fill="none" stroke="#fff" stroke-width="1.3"/></svg>
  <svg class="arrow next" width="8" height="14" viewBox="0 0 8 14"><path d="M1 1l6 6-6 6" fill="none" stroke="#fff" stroke-width="1.3"/></svg>
  <div class="wrap">
    <h2>Whats Our Clients Says</h2>
    <h3>Marcus Whitfield</h3>
    <div class="role">Managing Member, Northfield Holdings</div>
    <p class="quote-text">Lorem Ipsum is simply dummy text of the printing and typesetting industry. Lorem Ipsum has been the industry's standard dummy text ever since the 1500s, when an unknown printer took a galley of type and scrambled it to make a type specimen book. It has survived not only five centuries, but also the leap into electronic typesetting, remaining essentially unchanged.</p>
    <div class="dots"><span></span><span></span><span class="on"></span></div>
  </div>
</section>

<footer class="site-footer">
  <div class="wrap">
    <div class="foot-brand">
      <div class="brand"><span class="brand-dot"></span>GOLDEN BALE</div>
      <p>Ready to start a new project or curious about our process? Drop us a note or give us a call. We are happy to answer any questions and provide a free consultation.</p>
    </div>
    <div class="foot-col foot-menu">
      <h4>Menu</h4>
      <ul><li>Home</li><li>About us</li><li>Feed</li><li>Badding</li><li>Contact</li></ul>
    </div>
    <div class="foot-col foot-contact">
      <h4>Contact Us</h4>
      <ul>
        <li>Golden Bale<br>12 Meadow Lane #3, Fairfield,<br>ST 00000</li>
        <li>555-014-2290</li>
        <li>info@goldenbale.example</li>
      </ul>
    </div>
    <div class="foot-col">
      <h4>Social Media</h4>
      <div class="socials"><span></span><span class="on"></span><span></span><span></span><span></span></div>
      <div class="subscribe-input">
        <svg width="10" height="8" viewBox="0 0 10 8"><rect x=".5" y=".5" width="9" height="7" fill="none" stroke="#f7941d"/><path d="M.5 .5L5 4.5 9.5 .5" fill="none" stroke="#f7941d"/></svg>
        Email Address
      </div>
      <div class="subscribe-btn">Subscribe Now</div>
    </div>
  </div>
</footer>
<div class="copyright">©2021 goldenbale. All Rights Reserved.</div>

</body>
</html>
```